依頼詳細
医院の役員の名刺を新しくしたいと思っております。
ピンクを基調としたシンプルなデザインでお願いします。
当院のロゴも入れて頂きたいです。
記載項目
表面 会社名・役職・氏名・住所・電話・FAX・mail
裏面 理事長のみ裏面は英語 その他は白紙で大丈夫です。
希望イメージ
シンプル 複雑
単色 カラフル
暗い 明るい
日常 高級
遊び心 厳粛
未来的 伝統的
女性的 男性的
希望する色
赤系
納品ファイル
補足説明
■ 選んだ理由

ピンクを基調としたグラデーションがきれいで、かつスッキリしたデザインが気に入りました。また実際に使われる先生方にも気に入ってもらえたのでこちらの提案を選ばせていただきました。

■ 提案者全員のお礼・コメント

提案してくださったみなさん、たくさんのご提案ありがとうございました。
とても素敵な提案ばかりで悩みましたが、こちらに決定させていただきました。

また依頼することもあるかと思いますので、今後ともよろしくお願い致します。
本当にありがとうございました。

```html
<!DOCTYPE html>
<html lang="ja">
<head>
<meta charset="utf-8">
<title>名刺 森川歯科クリニック</title>
<link rel="stylesheet" href="https://fonts.googleapis.com/css2?family=Noto+Serif+JP:wght@400;500;700&display=swap">
<style>
  :root {
    --paper: #ffffff;
    --ink: #1a1a1a;
    --rose: #d9a3b4;
    --rose-deep: #c9809a;
  }
  html, body {
    margin: 0;
    padding: 0;
    width: 776px;
    height: 1200px;
    overflow: hidden;
    background: var(--paper);
  }
  .card {
    position: relative;
    width: 776px;
    height: 1200px;
    background: var(--paper);
    font-family: "Noto Serif JP", serif;
    color: var(--ink);
  }
  .card-frame {
    position: absolute;
    left: 31px;
    top: 26px;
    width: 712px;
    height: 1140px;
    border: 3px solid var(--rose);
    box-sizing: border-box;
  }
  .vertical {
    position: absolute;
    writing-mode: vertical-rl;
    white-space: nowrap;
  }
  .job-title {
    left: 385px;
    top: 52px;
    font-size: 27px;
    letter-spacing: 2px;
  }
  .person-name {
    left: 320px;
    top: 78px;
    font-size: 54px;
    font-weight: 500;
    letter-spacing: 10px;
  }
  .person-name .gap { display: inline-block; height: 60px; }
  .romaji {
    left: 290px;
    top: 80px;
    font-size: 22px;
    letter-spacing: 1px;
  }
  .romaji .gap { display: inline-block; height: 150px; }
  .contact {
    position: absolute;
    left: 200px;
    top: 740px;
    width: 520px;
    font-size: 22px;
    line-height: 31px;
    white-space: nowrap;
  }
  .contact p { margin: 0; }
  .contact .postal { padding-left: 148px; }
  .contact .phone, .contact .mail { padding-left: 18px; }
  .contact .mail { padding-left: 40px; }
  .clinic {
    position: absolute;
    left: 72px;
    top: 955px;
    display: flex;
    align-items: center;
    gap: 34px;
  }
  .clinic-mark {
    width: 90px;
    height: 90px;
    border-radius: 50%;
    background: var(--rose-deep);
    flex: none;
  }
  .clinic-group {
    margin: 0;
    font-size: 33px;
    font-weight: 500;
    letter-spacing: 2px;
  }
  .clinic-name {
    margin: 2px 0 0;
    font-size: 42px;
    font-weight: 700;
    letter-spacing: 5px;
  }
</style>
</head>
<body>
  <div class="card">
    <div class="card-frame"></div>

    <div class="vertical job-title">理事長</div>
    <div class="vertical person-name">森川<span class="gap"></span>直樹</div>
    <div class="vertical romaji">Naoki<span class="gap"></span>Morikawa</div>

    <div class="contact">
      <p class="postal">〒530-0012</p>
      <p>大阪府大阪市北区梅田町3-421 グランツ梅田2F</p>
      <p class="phone">tel/06-1234-5678　fax/06-0000-0000</p>
      <p class="mail">n_morikawa@morikawa-dc.jp</p>
    </div>

    <div class="clinic">
      <div class="clinic-mark"></div>
      <div>
        <p class="clinic-group">医療法人 明和会</p>
        <p class="clinic-name">森川歯科クリニック</p>
      </div>
    </div>
  </div>
</body>
</html>
```